Business card design for Virtual Assistance company

I need a business card designed for my virtual assistance company. We are a small company who services primarily C-level executive clients. The card needs to be double sided with the following contact information on the back:
Melissa Hartwell
Owner/CEO
info@pkrsolutions.net
www.pkrsolutions.net
310.552.9083

The front side should just have the company name incorporated: "PKR Solutions" and "virtual assistance"

The card should be simplistic, but eye catching and should speak to high level executives. Our primary focus areas consist of executive assistance and government contracting.

Target Market(s)

CEOs and executives

Contact Information for Business Card

see project description. phone, email, website.

Colors

Designer to choose only greyscale colors for use in the design.

```html
<!DOCTYPE html>
<html lang="en">
<head>
<meta charset="utf-8">
<title>PKR Solutions – Business Card</title>
<link href="https://fonts.googleapis.com/css2?family=Cinzel:wght@600&family=Poppins:wght@400;500&display=swap" rel="stylesheet">
<style>
  :root {
    --bg: #262626;
    --card-white: #ffffff;
    --charcoal: #222222;
    --charcoal-deep: #161616;
    --graphite: #3a3a3a;
    --sheen: #8a8a8a;
    --grey: #8c8c8c;
    --rule: #b0b0b0;
    --ink: #2a2a2a;
    --white: #ffffff;
  }
  * { margin: 0; padding: 0; box-sizing: border-box; }
  html, body {
    width: 1200px; height: 1108px; overflow: hidden;
    background: var(--bg);
  }
  .stage {
    position: relative; width: 1200px; height: 1108px;
    display: flex; justify-content: center; align-items: center; gap: 60px;
  }
  .card {
    position: relative; width: 440px; height: 740px;
    border-radius: 24px; overflow: hidden;
  }
  .card--front {
    background: var(--card-white);
    display: flex; flex-direction: column; align-items: center;
  }
  .brand { margin-top: 150px; text-align: center; }
  .brand__name {
    font-family: "Cinzel", serif; font-weight: 600;
    font-size: 40px; letter-spacing: 1px; color: var(--charcoal);
    white-space: nowrap;
  }
  .brand__tagline {
    display: flex; align-items: center; gap: 12px; justify-content: center;
    margin-top: 10px;
    font-family: "Poppins", sans-serif; font-size: 14px; letter-spacing: 4px;
    color: var(--grey); text-transform: uppercase;
  }
  .brand__tagline::before, .brand__tagline::after {
    content: ""; width: 30px; height: 2px; background: var(--rule);
  }
  .contact { margin-top: auto; margin-bottom: 120px; text-align: center; }
  .contact__name {
    font-family: "Cinzel", serif; font-weight: 600; font-size: 24px;
    color: var(--charcoal); letter-spacing: 1px;
  }
  .contact__role {
    font-family: "Poppins", sans-serif; font-size: 17px; color: var(--ink);
    margin-top: 2px;
  }
  .contact__icons {
    display: flex; align-items: center; gap: 6px; justify-content: center;
    margin: 12px 0 14px;
  }
  .contact__icons::before, .contact__icons::after {
    content: ""; width: 90px; height: 1px; background: var(--rule); margin: 0 10px;
  }
  .icon { width: 28px; height: 28px; }
  .icon__tile { fill: var(--charcoal); }
  .contact__line {
    font-family: "Poppins", sans-serif; font-size: 17px; color: var(--ink);
    line-height: 1.35;
  }
  .contact__line--web { color: var(--charcoal); }
  .card--back {
    background: linear-gradient(155deg, var(--charcoal-deep) 0%, var(--charcoal) 55%, var(--graphite) 100%);
  }
  .back__pattern {
    position: absolute; inset: 0;
    background:
      linear-gradient(205deg, rgba(160,160,160,0.45) 0%, rgba(110,110,110,0.18) 30%, rgba(30,30,30,0) 58%),
      repeating-linear-gradient(-25deg, rgba(255,255,255,0.035) 0 18px, rgba(0,0,0,0.05) 18px 44px),
      linear-gradient(20deg, rgba(0,0,0,0.35) 0%, rgba(0,0,0,0) 40%);
  }
  .back__mark {
    position: absolute; left: 250px; bottom: 190px;
    font-family: "Poppins", sans-serif; font-weight: 500; font-size: 18px;
    color: var(--white); white-space: nowrap;
  }
</style>
</head>
<body>
<main class="stage">
  <section class="card card--front">
    <header class="brand">
      <h1 class="brand__name">PKR Solutions</h1>
      <p class="brand__tagline">Virtual Assistance</p>
    </header>
    <div class="contact">
      <h2 class="contact__name">MELISSA HARTWELL</h2>
      <p class="contact__role">Owner/CEO</p>
      <div class="contact__icons">
        <svg class="icon" viewBox="0 0 28 28" aria-label="phone">
          <rect class="icon__tile" width="28" height="28" rx="4"/>
          <path d="M8 11c0-2 2-3 6-3s6 1 6 3v1h-3v-1.5h-6V12H8z M9 14h10l1 6H8z" fill="#fff"/>
        </svg>
        <svg class="icon" viewBox="0 0 28 28" aria-label="email">
          <rect class="icon__tile" width="28" height="28" rx="4"/>
          <rect x="6" y="9" width="16" height="11" fill="none" stroke="#fff" stroke-width="1.5"/>
          <path d="M6 9l8 6 8-6" fill="none" stroke="#fff" stroke-width="1.5"/>
        </svg>
        <svg class="icon" viewBox="0 0 28 28" aria-label="website">
          <rect class="icon__tile" width="28" height="28" rx="4"/>
          <circle cx="14" cy="14" r="8" fill="none" stroke="#fff" stroke-width="1.5"/>
          <path d="M6 14h16 M14 6c-4 4-4 12 0 16 M14 6c4 4 4 12 0 16" fill="none" stroke="#fff" stroke-width="1.2"/>
        </svg>
      </div>
      <p class="contact__line">310.552.9083</p>
      <p class="contact__line">info@pkrsolutions.net</p>
      <p class="contact__line contact__line--web">www.pkrsolutions.net</p>
    </div>
  </section>
  <section class="card card--back">
    <div class="back__pattern" role="img" aria-label="Embossed tonal repeating monogram pattern in charcoal with a soft grey sheen"></div>
    <p class="back__mark">PKR Solutions</p>
  </section>
</main>
</body>
</html>
```